Trade show booth design in Vector format.

Hello, I need a tradeshow booth design for a company called Corvalin. I am in need of a background for a dental trade show I will be doing in 10 days. The format is 90" by 90" with a .25 bleed.

Here are my 2 websites with the products and services I offer, I think this can give you a good idea of the colors and styles of font we like.

www.clearpathflo.ca

http://corvalin.sitebuildr.com

I'm thinking the type of theme of the background being the water theme I posted 1.1 MB file - with the phrase

"Des Solutions de traitement de l'eau efficaces et fiables pour votre clinique dentaire"

As the title text.

- with my 2 comapny logos integrated.

I am in need of this ASAP, so lets get going.

Gustavo

Target Market(s)

Dentists

Industry/Entity Type

Water Purification

Font styles to use
Sans Serif

Colors
33a6d7
85cae6
cee9f5
0692cd

Requirements
Must have
• My 2 logos - for my 2 companies.
• The slogan
• Des Solutions de traitement de l'eau efficaces et fiables pour votre clinique dentaire

```html
<!DOCTYPE html>
<html lang="fr">
<head>
<meta charset="utf-8">
<title>Corvalin – Stand salon dentaire</title>
<link rel="stylesheet" href="https://fonts.googleapis.com/css2?family=Open+Sans:wght@700&family=Questrial&display=swap">
<style>
  :root {
    --ink: #2272a7;
    --brand-teal: #5bbfc6;
    --water-light: #8ee0dc;
    --water-mid: #3fb4c4;
    --water-deep: #0f6fae;
    --paper: #ffffff;
  }
  html, body {
    margin: 0;
    padding: 0;
    width: 1200px;
    height: 1200px;
    overflow: hidden;
    background: var(--paper);
  }
  .booth {
    position: relative;
    width: 1200px;
    height: 1200px;
    background: var(--paper);
    overflow: hidden;
  }
  .brand {
    position: absolute;
    color: var(--brand-teal);
    font-family: "Questrial", sans-serif;
  }
  .brand--corvalin {
    left: 838px;
    top: 112px;
    font-size: 26px;
    letter-spacing: 0.5px;
    line-height: 1;
  }
  .brand--clearpath {
    left: 1000px;
    top: 100px;
    display: flex;
    align-items: center;
    gap: 10px;
  }
  .brand--clearpath .brand-square {
    flex: none;
    width: 18px;
    height: 18px;
    background: var(--brand-teal);
  }
  .brand--clearpath .brand-name {
    font-size: 16px;
    letter-spacing: 0.5px;
    text-transform: uppercase;
    line-height: 1.2;
  }
  .headline {
    position: absolute;
    left: 100px;
    top: 216px;
    margin: 0;
    color: var(--ink);
    font-weight: normal;
  }
  .headline-strong {
    display: block;
    font-family: "Open Sans", sans-serif;
    font-weight: 700;
    font-size: 80px;
    line-height: 94px;
    letter-spacing: 0.5px;
    white-space: nowrap;
  }
  .headline-strong .lower { text-transform: none; }
  .headline-light {
    display: block;
    font-family: "Questrial", sans-serif;
    font-size: 94px;
    line-height: 90px;
    margin-top: 8px;
    white-space: nowrap;
  }
  .water {
    position: absolute;
    left: 0;
    bottom: 0;
    width: 1200px;
    height: 345px;
  }
</style>
</head>
<body>
<div class="booth">
  <div class="brand brand--corvalin">corvalin</div>
  <div class="brand brand--clearpath">
    <span class="brand-square"></span>
    <span class="brand-name">ClearPath<br>Flo</span>
  </div>

  <h1 class="headline">
    <span class="headline-strong">DES SOLUTIONS <span class="lower">de</span></span>
    <span class="headline-strong">TRAITEMENT <span class="lower">de</span></span>
    <span class="headline-strong">L'EAU EFFICASES</span>
    <span class="headline-light">et fiables pour<br>votre clinique<br>dentaire</span>
  </h1>

  <svg class="water" viewBox="0 0 1200 345" role="img" aria-label="Photo sous-marine d'une vague d'eau turquoise avec bulles">
    <defs>
      <linearGradient id="waterFill" x1="0" y1="0" x2="0" y2="1">
        <stop offset="0" stop-color="var(--water-light)"/>
        <stop offset="0.45" stop-color="var(--water-mid)"/>
        <stop offset="1" stop-color="var(--water-deep)"/>
      </linearGradient>
    </defs>
    <path d="M0 160 C120 130 260 95 380 45 C440 20 520 15 600 30 C720 60 860 50 980 65 C1080 78 1150 72 1200 68 L1200 345 L0 345 Z" fill="url(#waterFill)"/>
  </svg>
</div>
</body>
</html>
```